Business Card Designs

Looking to design a 3.5" x 2" standard business card for our employees.
The design needs to be sleek, simple, and modern. We would like our logo (attached) to be incorporated, but not in that colour, rather an outline of the logo in either gold or silver (whichever looks better).

Modern and Simple is what we are looking for, but be creative in incorporating the logo.

```html
<!DOCTYPE html>
<html lang="en">
<head>
<meta charset="utf-8">
<title>Harbourline Suites — Business Card</title>
<link rel="stylesheet" href="https://fonts.googleapis.com/css2?family=Bebas+Neue&family=Oswald:wght@400;500&display=swap">
<style>
  :root {
    --bg: #c9c9c9;
    --card: #000000;
    --gold: #c9a030;
    --gold-light: #e4c45a;
    --gold-dark: #7a5f16;
  }
  * { box-sizing: border-box; margin: 0; padding: 0; }
  html, body { width: 900px; height: 1200px; overflow: hidden; }
  body { background: var(--bg); position: relative; }

  .card {
    position: absolute;
    top: 493px;
    width: 373px;
    height: 213px;
    background: var(--card);
    color: var(--gold);
    overflow: hidden;
  }
  .card--front { left: 60px; }
  .card--back { left: 466px; box-shadow: 0 2px 10px rgba(0,0,0,0.35); }

  .brand {
    position: absolute;
    display: flex;
    align-items: center;
    gap: 5px;
    font-family: "Bebas Neue", sans-serif;
    color: var(--gold);
    letter-spacing: 0.06em;
    white-space: nowrap;
  }
  .brand__mark { display: block; background: var(--gold); }

  .card--front .brand { left: 40px; top: 112px; font-size: 15px; }
  .card--front .brand__mark { width: 9px; height: 9px; }

  .rule { position: absolute; height: 1px; background: var(--gold); }
  .card--front .rule { left: 25px; right: 22px; top: 164px; }

  .website {
    position: absolute;
    left: 29px;
    top: 174px;
    font-family: "Oswald", sans-serif;
    font-weight: 500;
    font-size: 7px;
    letter-spacing: 0.22em;
    text-transform: uppercase;
  }

  .card--back .brand { left: 24px; top: 22px; font-size: 9px; }
  .card--back .brand__mark { width: 6px; height: 6px; }

  .title {
    position: absolute;
    left: 24px;
    top: 88px;
    font-family: "Bebas Neue", sans-serif;
    font-size: 29px;
    line-height: 1;
    color: var(--gold-light);
    letter-spacing: 0.01em;
    white-space: nowrap;
  }

  .info-row {
    position: absolute;
    left: 24px;
    display: flex;
    align-items: center;
    gap: 5px;
    font-family: "Oswald", sans-serif;
    font-size: 5px;
    letter-spacing: 0.12em;
    text-transform: uppercase;
    white-space: nowrap;
  }
  .info-row--address { top: 120px; }
  .info-row--contact { top: 176px; gap: 4px; }
  .info-item { display: flex; align-items: center; gap: 3px; }
  .info-item + .info-item { margin-left: 10px; }
  .info-divider { width: 1px; height: 8px; background: var(--gold); margin: 0 4px; }
  .info-row svg { width: 6px; height: 6px; fill: var(--gold); flex: none; }

  .card--back .rule { left: 24px; width: 203px; top: 164px; }

  .skyline-art {
    position: absolute;
    right: 0;
    top: 18px;
    width: 73px;
    height: 195px;
    background: linear-gradient(180deg, rgba(228,196,90,0.0) 0%, rgba(201,160,48,0.35) 45%, rgba(122,95,22,0.55) 100%);
  }
</style>
</head>
<body>

  <section class="card card--front">
    <div class="brand"><span class="brand__mark"></span>Harbourline Suites</div>
    <div class="rule"></div>
    <p class="website">www.harbourlinesuites.com</p>
  </section>

  <section class="card card--back">
    <div class="brand"><span class="brand__mark"></span>Harbourline Suites</div>
    <h1 class="title">HARBOURLINE SUITES</h1>

    <div class="info-row info-row--address">
      <span class="info-item">
        <svg viewBox="0 0 10 10"><path d="M5 0a3.5 3.5 0 0 0-3.5 3.5C1.5 6 5 10 5 10s3.5-4 3.5-6.5A3.5 3.5 0 0 0 5 0zm0 5a1.5 1.5 0 1 1 0-3 1.5 1.5 0 0 1 0 3z"/></svg>
        12 Lakeview Ave, Suite 300, Springfield, ON A1B 2C3
      </span>
      <span class="info-divider"></span>
      <span class="info-item">
        <svg viewBox="0 0 10 10"><path d="M5 0a5 5 0 1 0 0 10A5 5 0 0 0 5 0zm0 1c.6 0 1.4 1.3 1.6 3H3.4C3.6 2.3 4.4 1 5 1zM1 5.5h1.9c.1 1.2.4 2.2.8 2.9A4 4 0 0 1 1 5.5zm0-1A4 4 0 0 1 3.7 1.6c-.4.7-.7 1.7-.8 2.9zm4 4.5c-.6 0-1.4-1.3-1.6-3.5h3.2C6.4 7.7 5.6 9 5 9zm1.3-.6c.4-.7.7-1.7.8-2.9H9a4 4 0 0 1-2.7 2.9zM7.1 4.5c-.1-1.2-.4-2.2-.8-2.9A4 4 0 0 1 9 4.5z"/></svg>
        www.harbourlinesuites.com
      </span>
    </div>

    <div class="rule"></div>

    <div class="info-row info-row--contact">
      <span class="info-item">
        <svg viewBox="0 0 10 10"><path d="M2 0l2 2.5-1.2 1.3c.6 1.3 1.7 2.4 3 3L7.1 5.6 10 7.6 8.6 10C4 10 0 6 0 1.4z"/></svg>
        (555) 010-2142
      </span>
      <span class="info-item">
        <svg viewBox="0 0 10 10"><path d="M2 0l2 2.5-1.2 1.3c.6 1.3 1.7 2.4 3 3L7.1 5.6 10 7.6 8.6 10C4 10 0 6 0 1.4z"/></svg>
        (555) 010-8483
      </span>
      <span class="info-item">
        <svg viewBox="0 0 10 10"><path d="M0 2h10v.8L5 6 0 2.8zm0 2 5 3.2L10 4v4H0z"/></svg>
        info@harbourlinesuites.com
      </span>
    </div>

    <div class="skyline-art" role="img" aria-label="Gold outline building skyline decoration"></div>
  </section>

</body>
</html>
```